Business Card Design Project

Need a business card that stands my education platform as a whole but

Target Market(s)

Parents, families, expats in the middle east.

Industry/Entity Type

Education

Contact Information for Business Card

www.brightsprout.ae
www.thehomenest.ae
www.thecarecirclehub.ae

+971543192704
rebecca@brightsprout.ae

Font styles to use
Serif

Requirements
Must have
• Logo's and contact details

```html
<!DOCTYPE html>
<html lang="en">
<head>
<meta charset="utf-8">
<title>Bright Sprout – Business Card</title>
<link rel="stylesheet" href="https://fonts.googleapis.com/css2?family=Tinos:wght@400;700&display=swap">
<style>
  :root {
    --backdrop: #d4d4d4;
    --paper: #ffffff;
    --orange: #e8854a;
    --teal: #3a7c95;
    --text-light: #ffffff;
  }
  * { margin: 0; padding: 0; box-sizing: border-box; }
  html, body {
    width: 1200px;
    height: 1000px;
    overflow: hidden;
    background: var(--backdrop);
    font-family: "Tinos", "Times New Roman", serif;
  }
  .canvas {
    position: relative;
    width: 1200px;
    height: 1000px;
  }
  .card {
    position: absolute;
    left: 322px;
    width: 561px;
    overflow: hidden;
  }
  .card--front {
    top: 116px;
    height: 353px;
    background: var(--paper);
  }
  .card--back {
    top: 532px;
    height: 348px;
    background: var(--teal);
  }
  .front__brand {
    position: absolute;
    left: 0;
    top: 0;
    width: 280px;
    height: 100%;
    display: flex;
    align-items: center;
    justify-content: center;
  }
  .front__contact {
    position: absolute;
    left: 280px;
    top: 0;
    width: 281px;
    height: 100%;
    background: var(--orange);
  }
  .contact-list {
    position: absolute;
    right: 56px;
    top: 107px;
    list-style: none;
    text-align: right;
    color: var(--text-light);
    font-weight: 700;
    font-size: 18.5px;
    line-height: 26px;
  }
  .contact-list .gap { margin-top: 10px; }
  .accent-bar {
    position: absolute;
    right: 0;
    top: 104px;
    width: 17px;
    height: 143px;
    background: var(--teal);
  }
  .brand {
    display: flex;
    align-items: center;
    gap: 8px;
    font-weight: 700;
    white-space: nowrap;
  }
  .brand__dot {
    border-radius: 50%;
    flex: none;
  }
  .brand--small { color: var(--teal); font-size: 22px; }
  .brand--small .brand__dot { width: 14px; height: 14px; background: var(--teal); }
  .back__brand {
    position: absolute;
    inset: 0;
    display: flex;
    align-items: center;
    justify-content: center;
  }
  .brand--large { color: var(--text-light); font-size: 40px; gap: 14px; }
  .brand--large .brand__dot { width: 26px; height: 26px; background: var(--text-light); }
</style>
</head>
<body>
<main class="canvas">
  <section class="card card--front" aria-label="Business card front">
    <div class="front__brand">
      <div class="brand brand--small"><span class="brand__dot"></span>Bright Sprout</div>
    </div>
    <div class="front__contact">
      <ul class="contact-list">
        <li>www.brightsprout.ae</li>
        <li>www.thehomenest.ae</li>
        <li>www.thecarecirclehub.ae</li>
        <li class="gap">+971543192704</li>
        <li>rebecca@brightsprout.ae</li>
      </ul>
      <span class="accent-bar"></span>
    </div>
  </section>

  <section class="card card--back" aria-label="Business card back">
    <div class="back__brand">
      <div class="brand brand--large"><span class="brand__dot"></span>Bright Sprout</div>
    </div>
  </section>
</main>
</body>
</html>
```